Business Card Design for Cybersecurity Company - Quorvent Systems

We need a business card design for our new cybersecurity company, Quorvent. We’re going for a clean, hi tech look that feels modern, premium, and trustworthy. We want a design that really stands out and makes people say WOW when we hand it over!

Quorvent delivers reliable IT support and managed services for small and mid sized businesses. We help companies stay secure, efficient, and connected through proactive monitoring, cybersecurity services, cloud management, and remote support.

Target Market(s)

Designers should target small and mid sized businesses that need dependable cybersecurity and IT support.

Industry/Entity Type

Cybersecurity, Managed Service Provider, IT services

Contact Information for Business Card

Contact information

Requirements
Must have
• The card should look clean, modern, and tech focused, with the Quorvent logo, clear contact info, and strong readability. It needs to feel premium and professional while still keeping a simple layout that fits a cybersecurity and IT brand.
Nice to have
• Nice to have elements include subtle touches that give the card a modern, tech feel, along with a layout that works well in different background styles.
Should not have
• The card should avoid clutter, loud graphics, or anything that takes attention away from the logo and contact details.

```html
<!DOCTYPE html>
<html lang="en">
<head>
<meta charset="utf-8">
<title>Quorvent Systems — Business Card</title>
<link href="https://fonts.googleapis.com/css2?family=Poppins:wght@300;400;500;600;700&display=swap" rel="stylesheet">
<style>
  :root {
    --page-bg: #2b2b2b;
    --card-dark: #161616;
    --card-light: #ffffff;
    --brand-blue: #1e8cff;
    --brand-indigo: #4a55e8;
    --brand-purple: #6a2fe0;
    --ink-white: #ffffff;
    --card-w: 640px;
    --card-h: 366px;
  }
  * { box-sizing: border-box; margin: 0; padding: 0; }
  html, body {
    width: 1200px; height: 875px; overflow: hidden;
    background: var(--page-bg);
    font-family: "Poppins", sans-serif;
  }
  .stage {
    width: 1200px; height: 875px;
    display: flex; flex-direction: column;
    align-items: center; justify-content: center; gap: 40px;
  }
  .card {
    position: relative;
    width: var(--card-w); height: var(--card-h);
    border-radius: 22px; overflow: hidden;
  }

  /* Front */
  .card--front {
    background: var(--card-dark);
    display: flex; align-items: center; justify-content: center;
  }
  .wordmark {
    display: flex; align-items: center; gap: 16px;
    color: var(--brand-indigo);
    font-weight: 600;
  }
  .wordmark__dot {
    width: 22px; height: 22px; border-radius: 50%;
    background: var(--brand-indigo);
  }
  .card--front .wordmark__name { font-size: 48px; letter-spacing: 0.5px; }

  /* Back */
  .card--back { background: var(--card-light); }
  .card--back .wordmark {
    position: absolute; left: 120px; top: 78px;
  }
  .card--back .wordmark__name { font-size: 36px; }
  .card--back .wordmark__dot { width: 18px; height: 18px; }

  .name-band {
    position: absolute; left: 0; right: 0; top: 202px; height: 80px;
    background: linear-gradient(90deg, var(--brand-purple) 0%, var(--brand-indigo) 60%, var(--brand-blue) 100%);
    display: flex; flex-direction: column; justify-content: center;
    padding-left: 210px; color: var(--ink-white);
  }
  .name-band__name { font-size: 25px; font-weight: 600; line-height: 1.1; }
  .name-band__role { font-size: 12px; font-weight: 400; margin-top: 4px; }

  .band-divider {
    position: absolute; left: 0; right: 0; top: 282px; height: 4px;
    background: var(--card-light);
  }

  .contact-band {
    position: absolute; left: 0; right: 0; top: 286px; bottom: 0;
    background: linear-gradient(90deg, var(--brand-blue) 0%, var(--brand-indigo) 50%, var(--brand-purple) 100%);
    display: flex; justify-content: space-between; align-items: center;
    padding: 0 34px; color: var(--ink-white);
    font-size: 13px; font-weight: 400;
  }
  .contact-list { list-style: none; display: flex; flex-direction: column; gap: 5px; }
  .contact-list li { display: flex; align-items: center; gap: 10px; }
  .contact-list--right li { justify-content: flex-end; }
  .contact-icon { width: 13px; height: 13px; flex: none; fill: var(--ink-white); }
</style>
</head>
<body>
<main class="stage">

  <section class="card card--front" aria-label="Card front">
    <div class="wordmark">
      <span class="wordmark__dot"></span>
      <span class="wordmark__name">Quorvent Systems</span>
    </div>
  </section>

  <section class="card card--back" aria-label="Card back">
    <div class="wordmark">
      <span class="wordmark__dot"></span>
      <span class="wordmark__name">Quorvent Systems</span>
    </div>

    <div class="name-band">
      <p class="name-band__name">Dana Whitfield</p>
      <p class="name-band__role">Owner | CEO | Quorvent Systems</p>
    </div>
    <div class="band-divider"></div>

    <div class="contact-band">
      <ul class="contact-list">
        <li>
          <svg class="contact-icon" viewBox="0 0 16 16" aria-hidden="true"><path d="M2 5c0-1.5 2.5-3 6-3s6 1.5 6 3v1.5h-3V5.2C10.3 4.9 9.2 4.8 8 4.8s-2.3.1-3 .4v1.3H2zM4 7h8l2 6H2z"/></svg>
          (855) 555-0142
        </li>
        <li>
          <svg class="contact-icon" viewBox="0 0 16 16" aria-hidden="true"><path d="M5 1h6a1 1 0 0 1 1 1v12a1 1 0 0 1-1 1H5a1 1 0 0 1-1-1V2a1 1 0 0 1 1-1zm.5 2v9h5V3zM8 12.6a.7.7 0 1 0 0 1.4.7.7 0 0 0 0-1.4z"/></svg>
          (813) 555-0187
        </li>
      </ul>
      <ul class="contact-list contact-list--right">
        <li>
          dana@quorvent.com
          <svg class="contact-icon" viewBox="0 0 16 16" aria-hidden="true"><path d="M1 3h14v10H1zm1.5 1.5v.3L8 8.6l5.5-3.8v-.3zm0 2.1v4.9h11V6.6L8 10.4z"/></svg>
        </li>
        <li>
          www.quorvent.com
          <svg class="contact-icon" viewBox="0 0 16 16" aria-hidden="true"><path d="M8 1a7 7 0 1 0 0 14A7 7 0 0 0 8 1zm0 1.5c.8 0 1.8 1.6 2.1 4.5H5.9C6.2 4.1 7.2 2.5 8 2.5zM2.6 7h1.8c.1-1.5.4-2.8.9-3.7A5.5 5.5 0 0 0 2.6 7zm8.1-3.7c.5.9.8 2.2.9 3.7h1.8a5.5 5.5 0 0 0-2.7-3.7zM2.6 9a5.5 5.5 0 0 0 2.7 3.7c-.5-.9-.8-2.2-.9-3.7zm3.3 0c.3 2.9 1.3 4.5 2.1 4.5s1.8-1.6 2.1-4.5zm5.7 0c-.1 1.5-.4 2.8-.9 3.7A5.5 5.5 0 0 0 13.4 9z"/></svg>
        </li>
      </ul>
    </div>
  </section>

</main>
</body>
</html>
```